M Zyvantics Buisness Cards

I need a technology focused clean business card for my employees. I have attached out logo to include in the mocks. We're a modern tech consulting firm that drives to interface humanity with technology in a truly cohesive fashion.

```html
<!DOCTYPE html>
<html lang="en">
<head>
<meta charset="utf-8">
<title>M Zyvantics Business Cards</title>
<link rel="stylesheet" href="https://fonts.googleapis.com/css2?family=Open+Sans:wght@400;600&display=swap">
<style>
  :root {
    --page: #ffffff;
    --frame-line: #9a9a9a;
    --card: #414042;
    --stripe: #808080;
    --stripe-dark: #1e1c1d;
    --ink: #6f6f70;
    --ink-light: #8a8a8b;
    --emboss-dark: #232223;
  }
  * { margin: 0; padding: 0; box-sizing: border-box; }
  html, body {
    width: 1200px;
    height: 1200px;
    overflow: hidden;
    background: var(--page);
    font-family: "Open Sans", sans-serif;
  }
  .sheet { position: relative; width: 1200px; height: 1200px; }
  .trim-frame {
    position: absolute;
    left: 220px;
    width: 761px;
    height: 477px;
    border: 1px solid var(--frame-line);
    background: var(--page);
  }
  .trim-frame--front { top: 98px; }
  .trim-frame--back { top: 625px; }
  .card {
    position: absolute;
    left: 16px;
    top: 16px;
    width: 727px;
    height: 443px;
    border-radius: 12px;
    background: var(--card);
    overflow: hidden;
  }
  .card__stripes { position: absolute; inset: 0; width: 727px; height: 443px; }
  .brand-vertical {
    position: absolute;
    left: 82px;
    top: 219px;
    transform: translate(-50%, -50%) rotate(-90deg);
    white-space: nowrap;
    font-size: 40px;
    font-weight: 600;
    letter-spacing: 1px;
    color: var(--ink-light);
  }
  .contact {
    position: absolute;
    left: 490px;
    top: 254px;
    transform: translateX(-50%);
    list-style: none;
    text-align: center;
    font-size: 23px;
    line-height: 30.5px;
    color: var(--ink);
    text-shadow: -1px -1px 0 var(--emboss-dark), 1px 1px 0 rgba(255,255,255,0.08);
    white-space: nowrap;
  }
  .brand-centered {
    position: absolute;
    left: 362px;
    top: 168px;
    transform: translate(-50%, -50%);
    white-space: nowrap;
    font-size: 66px;
    font-weight: 600;
    letter-spacing: 1px;
    color: var(--ink);
  }
</style>
</head>
<body>
<main class="sheet">

  <section class="trim-frame trim-frame--front" aria-label="Card front">
    <div class="card">
      <svg class="card__stripes" viewBox="0 0 727 443" aria-hidden="true">
        <polygon points="161,0 175,0 175,270 161,283" fill="var(--stripe)"/>
        <polygon points="191,173 207,160 207,443 191,443" fill="var(--stripe)"/>
      </svg>
      <div class="brand-vertical">M Zyvantics</div>
      <ul class="contact">
        <li>John Smith</li>
        <li>job/position</li>
        <li>name@example.com</li>
        <li>555.555.555</li>
        <li>example.com</li>
      </ul>
    </div>
  </section>

  <section class="trim-frame trim-frame--back" aria-label="Card back">
    <div class="card">
      <svg class="card__stripes" viewBox="0 0 727 443" aria-hidden="true">
        <defs>
          <linearGradient id="stripe-fade" x1="0" y1="0" x2="1" y2="0">
            <stop offset="0" stop-color="#6b6b6c"/>
            <stop offset="0.45" stop-color="#58575a"/>
            <stop offset="1" stop-color="var(--stripe-dark)"/>
          </linearGradient>
          <linearGradient id="stripe-soft" x1="0" y1="0" x2="1" y2="0">
            <stop offset="0" stop-color="#7a7a7b"/>
            <stop offset="1" stop-color="#666667"/>
          </linearGradient>
        </defs>
        <polygon points="265,313 727,313 727,327 292,327" fill="url(#stripe-fade)"/>
        <polygon points="0,346 432,346 462,359 0,359" fill="url(#stripe-soft)"/>
      </svg>
      <div class="brand-centered">M Zyvantics</div>
    </div>
  </section>

</main>
</body>
</html>
```